Meridale Hair Studio Needs a new appointment business card

We need a new appointment card for our hair salon.

I Dont want bright out there colours.
I would like it to be neat, clean, easy to read. White, Black, with a hint of colour if needed.

We need
-Logo
-Phone number 47260385
-Mobile Number: 0417360528
Address: Shop 3/217 Tarrow Street, Kelby Court, Carrowby 4812

BACK SIDE OF CARD
- Appointment Time & Date (White background so we are able to write on it)
(If you are unable to make your appointment please contact us ASAP 47260385)

I also would like the chatterly and Snapfold logo(Find us on Chatterly)(find us on Snapfold)

Target Market(s)

appointment card simple to read. all information for their next appoint For all our clients male and female

Industry/Entity Type

Hairdresser

Contact Information for Business Card

-Logo
-Phone number 47260385

BACK SIDE OF CARD

Font styles to use
Serif
Sans Serif
Script

Requirements
Must have
• White Back ground on backside with appointment deatils so we are able to write information (like appointment time and date)
Nice to have
• Find us on Chatterly
and
snapfold - meridale_hairstudio
Should not have
• BRIGHT COLOURS

```html
<!DOCTYPE html>
<html lang="en">
<head>
<meta charset="utf-8">
<title>Meridale Hair Studio – Appointment Card</title>
<link href="https://fonts.googleapis.com/css2?family=Poppins:wght@400;500&display=swap" rel="stylesheet">
<style>
  :root {
    --backdrop: #d8d8d8;
    --ink: #111111;
    --paper: #ffffff;
    --card-black: #0b0b0b;
    --rule-light: #cfcfcf;
  }
  * { margin: 0; padding: 0; box-sizing: border-box; }
  html, body {
    width: 1200px;
    height: 800px;
    overflow: hidden;
    background: var(--backdrop);
    font-family: "Poppins", sans-serif;
  }
  .canvas { position: relative; width: 1200px; height: 800px; }

  .card {
    position: absolute;
    top: 283px;
    width: 427px;
    height: 238px;
  }
  .card-front { left: 112px; background: var(--card-black); color: var(--paper); }
  .card-back  { left: 638px; background: var(--paper); color: var(--ink); }

  .wordmark {
    position: absolute;
    left: 0; right: 0;
    text-align: center;
    font-weight: 500;
    line-height: 1;
  }
  .wordmark-name { display: block; letter-spacing: 0.04em; }
  .wordmark-tag  { display: block; letter-spacing: 0.22em; }

  .card-front .wordmark { top: 96px; }
  .card-front .wordmark-name { font-size: 34px; }
  .card-front .wordmark-tag  { font-size: 11px; margin-top: 6px; }

  .card-back .wordmark { top: 31px; }
  .card-back .wordmark-name { font-size: 19px; }
  .card-back .wordmark-tag  { font-size: 6.5px; margin-top: 3px; }

  .contact-numbers {
    position: absolute;
    left: 26px;
    top: 189px;
    display: flex;
    align-items: center;
    gap: 6px;
    font-size: 10px;
  }
  .contact-numbers .number { display: inline-flex; align-items: center; gap: 4px; }
  .contact-numbers svg { width: 8px; height: 8px; fill: var(--paper); }

  .contact-rule {
    position: absolute;
    left: 28px;
    width: 371px;
    top: 204px;
    border-top: 1px solid var(--rule-light);
  }
  .contact-address {
    position: absolute;
    right: 27px;
    top: 209px;
    font-size: 10px;
  }

  .appointment-fields {
    position: absolute;
    top: 89px;
    left: 25px;
    display: flex;
    align-items: baseline;
    font-size: 10px;
  }
  .field-line {
    display: inline-block;
    border-bottom: 1px solid var(--ink);
    height: 10px;
    position: relative;
    top: 2px;
  }
  .field-sep { margin: 0 1px; }
  .appointment-note {
    position: absolute;
    left: 0; right: 0;
    top: 213px;
    text-align: center;
    font-size: 9px;
  }
</style>
</head>
<body>
<main class="canvas">

  <section class="card card-front" aria-label="Card front">
    <div class="wordmark">
      <span class="wordmark-name">MERIDALE</span>
      <span class="wordmark-tag">HAIR-STUDIO</span>
    </div>

    <div class="contact-numbers">
      <span class="number">
        <svg viewBox="0 0 24 24" aria-hidden="true"><path d="M6.6 10.8a15.1 15.1 0 0 0 6.6 6.6l2.2-2.2a1 1 0 0 1 1-.25 11.4 11.4 0 0 0 3.6.57 1 1 0 0 1 1 1V20a1 1 0 0 1-1 1A17 17 0 0 1 3 4a1 1 0 0 1 1-1h3.5a1 1 0 0 1 1 1c0 1.25.2 2.45.57 3.6a1 1 0 0 1-.25 1z"/></svg>
        47260385
      </span>
      <span class="number">
        <svg viewBox="0 0 24 24" aria-hidden="true"><path d="M7 1h10a2 2 0 0 1 2 2v18a2 2 0 0 1-2 2H7a2 2 0 0 1-2-2V3a2 2 0 0 1 2-2zm0 3v15h10V4zm5 16.2a1 1 0 1 0 0 2 1 1 0 0 0 0-2z"/></svg>
        0417360528
      </span>
    </div>
    <div class="contact-rule"></div>
    <p class="contact-address">Shop 3/217 Tarrow Street, Kelby Court, Carrowby 4812</p>
  </section>

  <section class="card card-back" aria-label="Card back">
    <div class="wordmark">
      <span class="wordmark-name">MERIDALE</span>
      <span class="wordmark-tag">HAIR-STUDIO</span>
    </div>

    <div class="appointment-fields">
      <span>Time&nbsp;</span>
      <span class="field-line" style="width:48px"></span>
      <span class="field-sep">:</span>
      <span class="field-line" style="width:48px"></span>
      <span>&nbsp;&nbsp;AM | PM</span>
      <span style="margin-left:26px">Date&nbsp;</span>
      <span class="field-line" style="width:42px"></span>
      <span class="field-sep">/</span>
      <span class="field-line" style="width:42px"></span>
      <span class="field-sep">/</span>
      <span class="field-line" style="width:56px"></span>
    </div>

    <p class="appointment-note">If you are unable to make your appointment please contact us ASAP 47260385</p>
  </section>

</main>
</body>
</html>
```